New look and feel for investment website

Hi

Our website needs a crisp and professional look and feel applying to it. Here’s the address: http://www.plumbvane.co.uk. Since posting the brief yesterday (Tuesday, 16 August), we've reduced the amount of content on the home page, which should make life a little easier for you. We will come back later today, with some points of reference in terms of sites we like the look of. (See below)

17 August, 1.20pm GMT. OK, comments generally on the designs submitted so far. Please keep in mind that images of graphs, piles of coins, paper money and pretty females are not what is required. Better to think in terms of abstract imagery instead. Ratios? Circles? Relationships? Patterns? Not money,sex,graphs etc. Hope that helps.

For guidance on look and feel, please refer to these sites, which we like:

http://www.belmorrow.co.uk/
http://www.qv.com/
https://www.tolverhampsley.com
https://www.marigatefunds.com
https://www.pkalune.com
Updates

Here's the Tern Harbor logo created in AI CS5.

Our market is professional financial advisers and relatively sophisticated private investors. The look and feel therefore should be slick and sophisticated - not 'lively' and lightweight, more like a banking site. Please read the brief again where we've added a list of websites that we really like the look of to get a better feel for what we're looking for. Thanks once again, we appreciate the work you're putting in.

It's essential that all the elements that are on the current home page be included on all new designs. 

We use a device in our e-mails which you may wish to incorporate in your design.

Target Market(s)

Professional financial advisers. People who know about investment and money.

Industry/Entity Type

Investment

Requirements
Should not have
• Graphs or people.

```html
<!DOCTYPE html>
<html lang="en">
<head>
<meta charset="utf-8">
<title>Tern Harbor – Value investing</title>
<link rel="stylesheet" href="https://fonts.googleapis.com/css2?family=Noto+Sans:wght@400;500&display=swap">
<style>
:root{
  --sheet:#ffffff;
  --text:#4a4a4a;
  --text-soft:#5c5c5c;
  --brand:#2f3a44;
  --link:#e98a00;
  --accent:#f28a00;
  --accent-dark:#e35f00;
  --hero-frame:#cfcfcf;
  --hero-dark:#1d1d1d;
  --hero-mid:#3a3a3a;
  --hero-text:#ececec;
  --box-top:#dfe4ea;
  --box-border:#d8dde3;
}
*{box-sizing:border-box;margin:0;padding:0}
html,body{width:1200px;height:1170px;overflow:hidden}
body{
  background:linear-gradient(90deg,#dfe6ee 0,#f4f6f9 98px,var(--sheet) 98px,var(--sheet) 1102px,#f4f6f9 1102px,#dfe6ee 100%);
  font-family:"Noto Sans",Verdana,sans-serif;color:var(--text);position:relative;
}
.sheet{position:absolute;left:98px;top:0;width:1004px;height:1170px;background:var(--sheet);box-shadow:0 0 6px rgba(0,0,0,.08)}
.brand{position:absolute;left:127px;top:26px}
.brand-name{font-family:"Noto Sans",sans-serif;font-weight:400;font-size:34px;letter-spacing:.5px;color:var(--brand);line-height:44px}
.top-nav{position:absolute;right:137px;top:15px;font-size:10.5px;letter-spacing:.7px;color:#555}
.top-nav a{color:#555;text-decoration:none;margin:0 6px}
.top-nav a:last-child{margin-right:0}
.register-btn{position:absolute;left:923px;top:38px;width:139px;height:42px;background:linear-gradient(#ff9a2a,var(--accent-dark));color:#fff;font-size:14.5px;letter-spacing:.3px;text-align:center;line-height:42px;text-decoration:none;box-shadow:0 4px 4px -2px rgba(0,0,0,.25)}
.hero{position:absolute;left:118px;top:89px;width:964px;height:267px;background:var(--hero-frame);padding:6px 7px 4px 7px}
.hero-inner{position:relative;width:100%;height:100%;background:radial-gradient(ellipse at 70% 40%,var(--hero-mid),var(--hero-dark) 70%)}
.hero-text{position:absolute;left:10px;top:26px;font-size:19.5px;line-height:25px;color:var(--hero-text);letter-spacing:.6px}
.hero-text p+p{margin-top:22px}
.hero-art{position:absolute;left:490px;top:0;width:460px;height:257px;background:radial-gradient(ellipse at 62% 55%,rgba(230,215,195,.55),rgba(150,120,80,.25) 40%,transparent 70%)}
.side-nav{position:absolute;left:118px;top:369px;width:218px;height:352px;background:linear-gradient(#e7ebf0,#fff 30%);border-radius:8px 8px 0 0;border-right:1px solid #eee}
.side-nav ul{list-style:none;padding-top:15px}
.side-nav li{height:30px;padding-left:17px;padding-right:8px;font-size:10.5px;line-height:10.5px;letter-spacing:.9px;color:#444;position:relative}
.side-nav li::before{content:"";position:absolute;left:6px;top:2px;width:4px;height:4px;border-right:1.5px solid #555;border-bottom:1.5px solid #555;transform:rotate(-45deg)}
.content{position:absolute;left:363px;top:381px;width:705px;color:var(--text-soft)}
.content h1{font-weight:400;font-size:13.5px;line-height:17px;color:#555;letter-spacing:.5px;margin-bottom:16px}
.content p{font-size:10.8px;line-height:14.4px;letter-spacing:.55px;margin-bottom:14px}
.content .lead{font-size:13.4px;line-height:17.5px;color:#555;letter-spacing:.6px;margin-bottom:11px}
.content .more{font-size:13px;letter-spacing:.5px;margin-bottom:10px}
.content .more a{color:var(--link);text-decoration:none}
.content h2{font-weight:400;font-size:13px;letter-spacing:.5px;color:#555;margin-bottom:2px}
.stat{position:absolute;width:225px;height:100px;border:1px solid var(--box-border);border-radius:4px;background:linear-gradient(#fff 55%,var(--box-top));padding:14px 7px;color:var(--accent);font-size:13px;line-height:17px;letter-spacing:.7px}
.stat::before{content:"";position:absolute;left:0;right:0;top:0;height:8px;background:linear-gradient(var(--box-top),#fff);border-radius:4px 4px 0 0}
.note{position:absolute;left:119px;top:1024px;width:960px;font-size:13px;line-height:17px;letter-spacing:.55px;color:#555}
.legal{position:absolute;left:120px;top:1085px;width:945px;font-size:10.8px;line-height:14.5px;letter-spacing:.5px;color:#555}
</style>
</head>
<body>
<div class="sheet"></div>

<header>
  <div class="brand"><span class="brand-name">Tern Harbor</span></div>
  <nav class="top-nav"><a href="#">Login</a>|<a href="#">Register for free</a>|<a href="#">Contact us</a>|<a href="#">Terms &amp; Conditions</a></nav>
  <a class="register-btn" href="#">Free Registration</a>
</header>

<section class="hero">
  <div class="hero-inner">
    <div class="hero-art" role="img" aria-label="Eggs resting in and beside a wicker basket on a dark background"></div>
    <div class="hero-text">
      <p>A potential return of 23.57 % a year from<br>America’s biggest</p>
      <p>businesses with the emphasis firmly on<br>capital preservation.</p>
    </div>
  </div>
</section>

<nav class="side-nav">
  <ul>
    <li>Home</li>
    <li>The Two Minute Guide</li>
    <li>Current holdings &amp; year to date results</li>
    <li>What's on the Watch list</li>
    <li>Other important statistics</li>
    <li>About the back testing model and the results</li>
    <li>History of all trades</li>
    <li>Your questions answered</li>
    <li>About our fundamental analysis and the Margin of Safety</li>
    <li>About value investing</li>
    <li>The Halvern 1000 Index and the Q&amp;M 500 index</li>
  </ul>
</nav>

<main class="content">
  <h1>A methodical, consistent, highly selective system-driven process for identifying, and investing in, undervalued stocks</h1>
  <p>The attractions of value investing need no explanation to those who subscribe to the concept. But it's impractical, if not impossible, for the private investor to implement the strategy (using direct holdings as distinct to collective funds) consistently. Although the data may be available, to undertake fundamental analysis regularly, on a reasonable number of stocks, takes a significant amount of time and effort.</p>
  <p>By definition - and depending on where you look and market conditions - undervalued businesses (stocks) are relatively scarce. So where does the value investor begin their search? Which and how many businesses must be scrutinised before one undervalued entity is found? And having identified a stock that's trading at less than its estimated fair value, will that be the case next week or next month? Fundamentals can change for the worse at any time, so without the benefit of regular analysis, how will the value investor know when to disinvest?</p>
  <p class="lead">Those problems - and others - are now solved: our software takes the hard work out of value investing by providing the quantitative analysis the value investor needs.</p>
  <p class="more">For more details and the results to date...<a href="#">please go here</a></p>
  <h2>Here's what we do:</h2>
  <p>Once a month, month in month out, our program scrutinises the key fundamentals of 1,000 large cap American companies which between them account for 92% of the US securities market.</p>
  <p>First of all, the program sifts through each of the 1,000 stocks searching for favourable arrays of fundamentals: that process usually filters out between 950 and 975 stocks. The software then applies a range of algorithms to the short-listed stocks to identify any which are trading at 35% (or more) below their estimated fair value. There are times when not one single stock on the shortlist satisfies that criteria. But when they do - and if there's room - those stocks are added to our portfolio.</p>
</main>

<div class="stat" style="left:118px;top:806px">Average, annualised compound return: 23.57 %</div>
<div class="stat" style="left:364px;top:806px;padding-top:16px">So far this year, the portfolio's return is: 13.49 %</div>
<div class="stat" style="left:609px;top:806px;padding-top:12px">Worst ever annual loss: -1.48 %; best ever annual gain: 69.77 %</div>
<div class="stat" style="left:857px;top:806px;padding-top:16px">Average return per trade including losing trades: 24.44 %</div>
<div class="stat" style="left:118px;top:920px;padding-top:14px">Maximum number of winning/ losing trades in a row: 11/4</div>
<div class="stat" style="left:364px;top:920px;padding-top:15px">Average number of days a stock stays in the portfolio: 287</div>
<div class="stat" style="left:609px;top:920px;padding-top:12px">An average of five trades a year and never more than five holdings at any one time</div>
<div class="stat" style="left:857px;top:920px;padding-top:16px">86 trades in total, of which 65 were profitable - a success rate of 75.58 %</div>

<p class="note">If you have any questions, please e-mail info@ternharbor.co.uk. Although we’re very willing to answer queries about the way we pick stocks, please do keep in mind that as we’re making this service available free of charge initially, we’re not inclined to expend time and energy debating the relative merits of value investing or fundamental analysis. Other than that, fire away!</p>

<footer class="legal">This website is published by Tern Harbor Ltd. Registered in England No. 08314527. Registered office: 41 Aldwick Crescent London N9 2QT. This website and its content is the copyright of Tern Harbor Ltd - © Tern Harbor Ltd 2011. All rights reserved. Any redistribution or reproduction of part or all of the contents in any form is prohibited other than the following: you may print or download to a local hard disk extracts for your personal and non-commercial use only you may copy the content to individual third parties for their personal use, but only if you acknowledge the website as the source of the material. You may not, except with our express written permission, distribute or commercially exploit the content. Nor may you transmit it or store it in any other website or other form of electronic retrieval system.</footer>
</body>
</html>
```